Whitmore Business Card Design

The name of the business is Dara Whitmore, CPA LLC
The service that we offer is Accounting, Tax & Consulting Services. I need it to have the following items:
Dara Whitmore, Principal
Phone Number
Email Address
Physical Address

I have attached the company logo, one in black and one in white. Please provide a design in black background and the other in white background. Please include "Accounting, Tax & Consulting Services". I want the business card to be clean and very professional.

```html
<!DOCTYPE html>
<html lang="en">
<head>
<meta charset="utf-8">
<title>Dara Whitmore, CPA LLC – Business Card</title>
<link rel="stylesheet" href="https://fonts.googleapis.com/css2?family=Bebas+Neue&family=Epilogue:ital,wght@0,400;0,600;0,700;1,500;1,600&display=swap">
<style>
  :root {
    --paper: #ffffff;
    --ink: #111111;
    --brand-red: #a11d1f;
    --brand-grey: #3d3d3d;
    --rule-grey: #9a9a9a;
    --motif-tint: #f7f6f6;
  }
  * { margin: 0; padding: 0; box-sizing: border-box; }
  html, body {
    width: 1200px;
    height: 1000px;
    overflow: hidden;
    background: var(--paper);
  }
  .card {
    position: relative;
    width: 1200px;
    height: 1000px;
    background: var(--paper);
    font-family: "Epilogue", "Helvetica Neue", Arial, sans-serif;
    color: var(--ink);
  }
  .backdrop-motif {
    position: absolute;
    left: 755px;
    top: 187px;
    width: 445px;
    height: 620px;
    background: var(--motif-tint);
  }
  .holder-name {
    position: absolute;
    left: 140px;
    top: 246px;
    font-family: "Bebas Neue", "Oswald", Impact, sans-serif;
    font-size: 92px;
    line-height: 1;
    letter-spacing: 0.5px;
    color: var(--ink);
    white-space: nowrap;
  }
  .holder-title {
    position: absolute;
    left: 141px;
    top: 336px;
    font-size: 38px;
    font-style: italic;
    font-weight: 600;
    line-height: 1;
  }
  .title-rule {
    position: absolute;
    left: 108px;
    top: 403px;
    width: 475px;
    height: 3px;
    background: var(--brand-red);
  }
  .contact-list {
    position: absolute;
    left: 141px;
    top: 448px;
    list-style: none;
    font-size: 31px;
    font-weight: 400;
    line-height: 1;
  }
  .contact-list li { height: 59px; }
  .firm-lockup {
    position: absolute;
    left: 370px;
    top: 678px;
    width: 460px;
  }
  .firm-mark {
    display: flex;
    align-items: center;
    gap: 20px;
  }
  .firm-square {
    width: 56px;
    height: 56px;
    background: var(--brand-grey);
    flex: none;
  }
  .firm-name {
    font-size: 25px;
    font-weight: 700;
    color: var(--brand-grey);
    white-space: nowrap;
  }
  .firm-rule {
    margin: 11px 0 0 27px;
    width: 405px;
    height: 2px;
    background: var(--rule-grey);
  }
  .firm-services {
    margin: 7px 0 0 27px;
    width: 405px;
    text-align: center;
    font-size: 20px;
    font-style: italic;
    font-weight: 500;
    color: var(--ink);
    white-space: nowrap;
  }
</style>
</head>
<body>
  <main class="card">
    <div class="backdrop-motif" role="img" aria-label="Faint enlarged firm monogram as background decoration"></div>

    <h1 class="holder-name">Dara Whitmore</h1>
    <p class="holder-title">Principal</p>
    <div class="title-rule"></div>

    <ul class="contact-list">
      <li>+000 12345 6789</li>
      <li>email@website.com</li>
      <li>Street address, here</li>
    </ul>

    <div class="firm-lockup">
      <div class="firm-mark">
        <span class="firm-square"></span>
        <span class="firm-name">Dara Whitmore, CPA LLC</span>
      </div>
      <div class="firm-rule"></div>
      <p class="firm-services">Accounting, Tax &amp; Consulting Services</p>
    </div>
  </main>
</body>
</html>
```